Harvesting Victors 6x9 book soft cover- front cover only

We need a book cover for a softcover book. We will need final files in Photoshop or InDesign is preferred.

Overall Title:
Harvesting Victors
Subtitle:
The Foundations of Humble Mentoring for Trainers, Instructors and Players
Author:
by Dr. Marcus Pettiford

The audience is high school and college coaches however we don't want the standard picture with words over the top. Make it a creative design but keep it mind it's a little academic.

```html
<!DOCTYPE html>
<html lang="en">
<head>
<meta charset="utf-8">
<title>Harvesting Victors — Front Cover</title>
<link rel="stylesheet" href="https://fonts.googleapis.com/css2?family=Montserrat:wght@400;500&family=Oswald:wght@500&display=swap">
<style>
  :root {
    --ink: #000000;
    --paper: #ffffff;
    --spot: #f7ec2b;
    --spot-soft: #fff7a8;
    --haze: #3a3a3a;
  }
  html, body {
    margin: 0;
    padding: 0;
    background: var(--ink);
    overflow: hidden;
  }
  .cover {
    position: relative;
    width: 800px;
    height: 1200px;
    background: var(--ink);
    overflow: hidden;
    font-family: "Montserrat", sans-serif;
    color: var(--paper);
  }
  .stage-lights {
    position: absolute;
    inset: 0;
    width: 800px;
    height: 1200px;
  }
  .hero-figure {
    position: absolute;
    left: 290px;
    top: 180px;
    width: 230px;
    height: 560px;
    background: linear-gradient(180deg, #0b0b0b 0%, #050505 100%);
    border-radius: 110px 110px 20px 20px;
  }
  .title {
    position: absolute;
    left: 0;
    width: 800px;
    top: 810px;
    margin: 0;
    text-align: center;
    font-weight: 500;
    line-height: 1;
    text-transform: uppercase;
  }
  .title-lead {
    display: block;
    font-size: 50px;
    letter-spacing: 1px;
  }
  .title-main {
    display: block;
    margin-top: 8px;
    font-size: 104px;
    letter-spacing: 1px;
  }
  .subtitle {
    position: absolute;
    left: 0;
    width: 800px;
    top: 985px;
    margin: 0;
    text-align: center;
    font-family: "Oswald", sans-serif;
    font-weight: 500;
    font-size: 34px;
    line-height: 42px;
    letter-spacing: 1px;
    color: var(--spot);
    text-transform: uppercase;
  }
  .author {
    position: absolute;
    left: 0;
    width: 800px;
    top: 1112px;
    margin: 0;
    text-align: center;
    font-weight: 400;
    font-size: 28px;
    letter-spacing: 4px;
    text-transform: uppercase;
  }
</style>
</head>
<body>
<main class="cover">
  <svg class="stage-lights" viewBox="0 0 800 1200" aria-hidden="true">
    <defs>
      <linearGradient id="beam-left" x1="0" y1="0" x2="1" y2="1">
        <stop offset="0" stop-color="var(--spot)"/>
        <stop offset="0.75" stop-color="var(--spot)"/>
        <stop offset="1" stop-color="var(--spot-soft)"/>
      </linearGradient>
      <linearGradient id="beam-right" x1="1" y1="0" x2="0" y2="1">
        <stop offset="0" stop-color="var(--spot)"/>
        <stop offset="0.75" stop-color="var(--spot)"/>
        <stop offset="1" stop-color="var(--spot-soft)"/>
      </linearGradient>
      <linearGradient id="floor-beam" x1="0" y1="1" x2="0" y2="0">
        <stop offset="0" stop-color="var(--haze)" stop-opacity="0.9"/>
        <stop offset="1" stop-color="var(--haze)" stop-opacity="0"/>
      </linearGradient>
      <radialGradient id="centre-glow" cx="0.5" cy="0.5" r="0.5">
        <stop offset="0" stop-color="#ffffff" stop-opacity="0.95"/>
        <stop offset="0.4" stop-color="var(--spot-soft)" stop-opacity="0.6"/>
        <stop offset="1" stop-color="var(--spot)" stop-opacity="0"/>
      </radialGradient>
    </defs>
    <polygon points="0,1200 230,1200 400,640" fill="url(#floor-beam)"/>
    <polygon points="800,1200 570,1200 400,640" fill="url(#floor-beam)"/>
    <polygon points="40,0 290,0 400,660" fill="url(#beam-left)"/>
    <polygon points="510,0 760,0 400,660" fill="url(#beam-right)"/>
    <ellipse cx="400" cy="640" rx="120" ry="70" fill="url(#centre-glow)"/>
  </svg>

  <div class="hero-figure" role="img" aria-label="Silhouette of a triumphant coach with raised fist, standing in the spotlights"></div>

  <h1 class="title">
    <span class="title-lead">Harvesting</span>
    <span class="title-main">Victors</span>
  </h1>

  <p class="subtitle">The Foundations of Humble Mentoring<br>for Trainers, Instructors and Players</p>

  <p class="author">Dr. Marcus Pettiford</p>
</main>
</body>
</html>
```